Post storm repair flyer

looking for an eye catching 6x9 postcard to send out to single family home owners advertising a "Post Storm Repair Special" explaining that after the recent hurricanes its very important to have your roof checked and any repairs fixed right away before they become a bigger more costly problem and that even though your home wasn't directly hit by the storm the high wind gust could've cause unseen damage.
offer $200 off any repair *some rules may apply
Lark Roofing
888.417.LARK
www.LarkRoofing.example

Roofing

```html
<!DOCTYPE html>
<html lang="en">
<head>
<meta charset="utf-8">
<title>Lark Roofing – Post Storm Repair Special</title>
<link href="https://fonts.googleapis.com/css2?family=League+Spartan:wght@400;500;600;700;800&display=swap" rel="stylesheet">
<style>
  :root {
    --yellow: #f9c80f;
    --yellow-soft: #f6dc5c;
    --charcoal: #434343;
    --grey-diamond: #767676;
    --white: #ffffff;
    --black: #0b0b0b;
    --red: #f41d0f;
    --backdrop: #dcdcdc;
  }
  * { margin: 0; padding: 0; box-sizing: border-box; }
  html, body {
    width: 1200px; height: 984px; overflow: hidden;
    background: var(--backdrop);
  }
  .postcard {
    position: absolute; left: 30px; top: 112px;
    width: 1682px; height: 1121px;
    transform: scale(0.6778); transform-origin: 0 0;
    background: var(--yellow);
    overflow: hidden;
    font-family: "League Spartan", Arial, sans-serif;
  }
  .backdrop-shapes, .photo { position: absolute; left: 0; top: 0; }
  .headline {
    position: absolute; right: 37px; top: 34px; text-align: right;
    color: var(--black); line-height: 1;
  }
  .headline-main { font-size: 76px; font-weight: 800; letter-spacing: 0.5px; }
  .headline-main .accent { color: var(--red); }
  .headline-sub { font-size: 70px; font-weight: 500; margin-top: 10px; }
  .storm-copy {
    position: absolute; left: 1249px; top: 187px; width: 397px;
    font-family: Arial, Helvetica, sans-serif; font-size: 25.5px; line-height: 33.8px;
    color: var(--black); text-align: justify; text-align-last: justify;
  }
  .corner-brand {
    position: absolute; left: 44px; top: 72px;
    display: flex; align-items: center; gap: 12px;
    color: var(--yellow); font-size: 30px; font-weight: 600;
  }
  .corner-brand .dot { width: 34px; height: 34px; border: 5px solid var(--yellow); border-radius: 50%; }
  .brand-name {
    position: absolute; left: 966px; top: 882px; width: 520px; text-align: center;
    color: var(--yellow); font-size: 84px; font-weight: 600; white-space: nowrap;
  }
  .contact {
    position: absolute; top: 1022px; display: flex; align-items: center; gap: 16px;
    color: var(--white); font-size: 37px; font-weight: 500; white-space: nowrap;
  }
  .contact-web { left: 726px; }
  .contact-phone { right: 37px; }
  .contact svg { width: 62px; height: 66px; flex: none; }
  .offer { position: absolute; left: 40px; top: 800px; color: var(--black); }
  .offer-label { color: var(--red); font-size: 46px; font-weight: 500; line-height: 1; }
  .offer-amount { font-size: 124px; font-weight: 800; line-height: 1; margin-top: 14px; letter-spacing: -2px; }
  .offer-off { font-size: 112px; font-weight: 800; line-height: 0.85; display: flex; align-items: flex-end; gap: 8px; }
  .offer-off .scope { font-size: 44px; font-weight: 500; line-height: 1; letter-spacing: 0; }
  .offer-terms { font-size: 27px; font-weight: 500; margin-top: 20px; }
</style>
</head>
<body>
<main class="postcard">
  <svg class="backdrop-shapes" width="1682" height="1121" viewBox="0 0 1682 1121" aria-hidden="true">
    <polygon points="0,0 535,0 0,308" fill="var(--charcoal)"/>
    <polygon points="0,308 467,40 960,326 960,652 467,945 0,677" fill="var(--white)"/>
    <polygon points="467,945 1233,490 1682,750 1682,1121 770,1121" fill="var(--charcoal)"/>
    <polygon points="1094,272 1229,195 1229,347" fill="var(--yellow-soft)"/>
    <polygon points="1505,588 1682,485 1682,690" fill="var(--yellow-soft)"/>
    <polygon points="549,943 674,869 799,943 674,1017" fill="var(--grey-diamond)"/>
    <polygon points="467,100 810,298 810,697 467,895 124,697 124,298" fill="var(--yellow-soft)"/>
    <polygon points="1042,272 1234,383 1234,600 1042,712 850,600 850,383" fill="var(--yellow-soft)"/>
  </svg>

  <svg class="photo" width="1682" height="1121" viewBox="0 0 1682 1121" role="img" aria-label="Photo of a two-storey house with its roof torn open and storm debris and fallen branches across the yard">
    <defs>
      <linearGradient id="storm-house" x1="0" y1="0" x2="0" y2="1">
        <stop offset="0" stop-color="#d9dadb"/>
        <stop offset="0.45" stop-color="#8c7f74"/>
        <stop offset="1" stop-color="#7a5a42"/>
      </linearGradient>
    </defs>
    <polygon points="467,112 800,304 800,691 467,883 134,691 134,304" fill="url(#storm-house)"/>
  </svg>

  <svg class="photo" width="1682" height="1121" viewBox="0 0 1682 1121" role="img" aria-label="Photo of a metal roof peeled off a brick building onto a parked car">
    <defs>
      <linearGradient id="peeled-roof" x1="0" y1="0" x2="1" y2="1">
        <stop offset="0" stop-color="#9fb3c4"/>
        <stop offset="0.55" stop-color="#6b7d8f"/>
        <stop offset="1" stop-color="#8a4a38"/>
      </linearGradient>
    </defs>
    <polygon points="1042,282 1226,388 1226,595 1042,702 858,595 858,388" fill="url(#peeled-roof)"/>
  </svg>

  <div class="corner-brand"><span class="dot"></span><span>LARK ROOFING</span></div>

  <header class="headline">
    <h1 class="headline-main">POST STORM REPAIR <span class="accent">SPECIAL</span></h1>
    <p class="headline-sub">FROM LARK ROOFING</p>
  </header>

  <p class="storm-copy">After any hurricanes its very important to have your roof checked and any repairs fixed right away before they become a bigger more costly problem and that even though your home wasn't directly hit by the storm the high wind gust could've cause unseen damage.</p>

  <section class="offer">
    <p class="offer-label">OFFER</p>
    <p class="offer-amount">$200</p>
    <p class="offer-off">OFF<span class="scope">ANY REPAIR</span></p>
    <p class="offer-terms">*SOME RULES MAY APPLY</p>
  </section>

  <p class="brand-name">LARK ROOFING</p>

  <p class="contact contact-web">
    <svg viewBox="0 0 62 66" aria-hidden="true">
      <polygon points="31,3 58,18 58,48 31,63 4,48 4,18" fill="var(--yellow)" stroke="var(--red)" stroke-width="4"/>
      <g fill="none" stroke="var(--charcoal)" stroke-width="2.6">
        <circle cx="31" cy="33" r="15"/>
        <ellipse cx="31" cy="33" rx="6.5" ry="15"/>
        <line x1="16" y1="33" x2="46" y2="33"/>
        <path d="M19 25 H43 M19 41 H43"/>
      </g>
    </svg>
    <span>WWW.LARKROOFING.EXAMPLE</span>
  </p>

  <p class="contact contact-phone">
    <svg viewBox="0 0 62 66" aria-hidden="true">
      <polygon points="31,3 58,18 58,48 31,63 4,48 4,18" fill="var(--yellow)" stroke="var(--red)" stroke-width="4"/>
      <circle cx="31" cy="33" r="16" fill="none" stroke="var(--charcoal)" stroke-width="2.6"/>
      <path d="M24 24 l4 -1 3 6 -3 2 q2 5 7 7 l2 -3 6 3 -1 4 q-3 2 -7 0 q-9 -4 -12 -13 q-1 -4 1 -5z" fill="none" stroke="var(--charcoal)" stroke-width="2.4" stroke-linejoin="round"/>
    </svg>
    <span>888.417.LARK</span>
  </p>
</main>
</body>
</html>
```